Velmarhomes.com requires a powerful call to action landing page to attract sellers in Ontario

We are a new Toronto based real estate company, starting an advertisement campaign online to get sellers and buyers.
This will be the landing page for them to view and submit their contact information.

This page should feature:
- Our Previous Sold Listings (which I will provide via email) Including high quality pictures
- An "explainer" video included on the page
- Fast to load, with high quality imaging
- A section of this page should include a contact/submit form for potential clients
- Company contact information
- Bottom of page will include testimonial videos from past clients

I would like the page to be very clean and minimalistic, I will be sending you a 2-300 word sales copy to be placed on the site.
Our design should reflect our logo colours, which will also be attached.

Our page should be elegant, luxurious looking and stand out from the competition.
Updates

Target Market(s)

Looking to target, people all over the Ontario looking to sell their homes.

Industry/Entity Type

Real Estate

Number of Pages Required

1 page

Requirements
Must have
• Header/cover to feature slide show of previous sold listings (see link below for listings) with high quality images (click virtual tour for each listing HQ images) and few details such as; rooms, bathrooms, city. Please also add a strong emphasis on listing detail such as; Days on market(DOM), List price and sold price, calculated over asking value in ($) (sold price minus list price)
• http://v3.quindrelistings.net/Live/Pages/Public/Link.aspx?Key=c493e51a88107fbe2364a9b1c6027d15&App=KPLO

```html
<!DOCTYPE html>
<html lang="en">
<head>
<meta charset="utf-8">
<title>Velmarhomes.com – Sell Your Home in Ontario</title>
<link href="https://fonts.googleapis.com/css2?family=Open+Sans:ital,wght@0,400;0,600;0,700;1,400&family=Courgette&display=swap" rel="stylesheet">
<style>
:root{
  --coral:#ee5a63;
  --red:#e3222e;
  --red-dark:#c81b27;
  --blush:#f7e4e4;
  --nav:#f1d5d6;
  --ink:#2b2b2b;
  --muted:#555;
  --dark:#2c2729;
  --white:#fff;
  --line:#ddd;
}
*{box-sizing:border-box;margin:0;padding:0}
html,body{width:1200px;height:2350px;overflow:hidden}
body{font-family:'Open Sans',Arial,sans-serif;color:var(--ink);background:var(--white);position:relative}
.abs{position:absolute}
.play{position:absolute;width:44px;height:44px;border-radius:50%;background:var(--red);display:flex;align-items:center;justify-content:center}
.play svg{width:16px;height:16px;margin-left:3px}
.play.sm{width:32px;height:32px}
.play.sm svg{width:12px;height:12px}

/* header */
.site-header{position:absolute;left:0;top:0;width:1200px;height:94px}
.brand{position:absolute;left:146px;top:28px;display:flex;align-items:center;gap:12px}
.brand-mark{width:38px;height:38px;background:var(--red)}
.brand-name{font-size:30px;font-weight:600;color:var(--ink);letter-spacing:-.5px}
.search{position:absolute;left:573px;top:27px;width:425px;height:43px;border:1px solid #ccc;display:flex;align-items:center;padding:0 18px;font-size:12.5px;color:#444;justify-content:space-between}
.nav{position:absolute;left:0;top:94px;width:1200px;height:58px;background:var(--nav)}
.nav a{position:absolute;top:20px;font-size:13px;color:#333;text-decoration:none}
.nav a.current{color:var(--red)}
.nav .dot{position:absolute;top:22px;width:15px;height:15px;border-radius:50%;background:#777}

/* hero */
.hero-panel{position:absolute;left:99px;top:152px;width:202px;height:401px;background:var(--coral);color:var(--white);padding:30px 22px}
.hero-price{font-family:'Courgette',cursive;font-size:29px;line-height:1.1}
.hero-price small{display:block;font-size:25px}
.hero-street{font-size:18px;margin-top:26px;white-space:nowrap}
.hero-facts{font-size:9.6px;line-height:25px;margin-top:10px;opacity:.95;white-space:nowrap}
.hero-btn{position:absolute;left:22px;top:272px;width:156px;height:51px;border:2px solid var(--white);display:flex;align-items:center;justify-content:center;font-size:15px}
.hero-dots{position:absolute;left:24px;top:362px;display:flex;gap:6px}
.hero-dots i{width:10px;height:10px;border-radius:50%;background:#f7c2c5}
.hero-dots i:first-child{background:var(--white)}
.hero-photo{position:absolute;left:301px;top:152px;width:800px;height:401px;background:linear-gradient(180deg,#6fa4d8 0%,#cbb07c 45%,#8f7348 70%,#4d7a35 100%)}

/* welcome */
.welcome h1{position:absolute;left:122px;top:588px;font-size:27px;font-weight:400}
.welcome p{position:absolute;left:122px;top:629px;width:590px;font-size:11px;line-height:25px;color:#444}
.btn-coral{position:absolute;background:var(--coral);color:var(--white);border-radius:6px;display:flex;align-items:center;justify-content:center;font-size:12px;font-weight:600}
.welcome .divider{position:absolute;left:736px;top:594px;width:1px;height:146px;background:var(--line)}
.explainer{position:absolute;left:780px;top:584px;width:298px;height:173px;border:1px solid #ddd;background:linear-gradient(135deg,#f2f2f2 0%,#cfd6de 50%,#d9a98f 100%)}
.explainer .bar{position:absolute;left:0;bottom:0;width:100%;height:18px;background:#eee;border-top:1px solid #ccc}
.explainer .bar b{position:absolute;left:30px;top:7px;width:130px;height:4px;background:#ccc}
.explainer .bar b::before{content:"";position:absolute;left:0;top:0;width:56px;height:4px;background:var(--red)}

/* sold */
.band-blush{position:absolute;left:0;width:1200px;background:var(--blush)}
.section-title{position:absolute;font-size:21px;font-weight:400;color:var(--ink)}
.media{position:absolute}
.sold-main{left:99px;top:871px;width:485px;height:237px;background:linear-gradient(90deg,#cfcfcf 0%,#9a9a9a 45%,#2a2a2a 75%,#555 100%)}
.sold-caption{position:absolute;left:0;bottom:0;width:100%;height:37px;background:rgba(0,0,0,.8);color:#eee;font-size:10.5px;display:flex;align-items:center;gap:18px;padding-left:46px}
.sold-thumb1{left:600px;top:871px;width:215px;height:110px;background:linear-gradient(135deg,#e2d4c0,#a07a55)}
.sold-thumb2{left:600px;top:997px;width:215px;height:111px;background:linear-gradient(135deg,#4a4a4a,#1d1d1d)}
.buyer-form{position:absolute;left:899px;top:788px;width:202px;height:367px;background:var(--dark)}
.buyer-form .head{height:77px;background:linear-gradient(180deg,var(--coral),#f0868c);color:var(--white);font-family:'Courgette',cursive;font-size:23px;line-height:29px;padding:10px 17px}
.field{position:absolute;left:20px;width:161px;height:26px;background:var(--white);font-size:10.5px;color:#333;padding:6px 8px}
.field.select::after{content:"";position:absolute;right:9px;top:10px;border:5px solid transparent;border-top-color:#333}
.buyer-form .submit{position:absolute;left:51px;top:313px;width:101px;height:31px;background:var(--coral);color:var(--white);font-weight:600;font-size:15px;display:flex;align-items:center;justify-content:center}

/* exclusive */
.carousel-arrows{position:absolute;left:1052px;top:1190px;display:flex;gap:4px}
.carousel-arrows span{width:22px;height:22px;border-radius:50%;background:#aaa;display:flex;align-items:center;justify-content:center}
.listing{position:absolute;top:1239px;width:241px}
.listing .photo{height:159px;position:relative}
.listing .nav-mini{position:absolute;right:6px;top:6px;display:flex;gap:2px}
.listing .nav-mini i{width:14px;height:14px;background:#222;display:block}
.listing h3{font-size:12px;font-weight:600;color:var(--coral);margin-top:10px}
.listing .row{font-size:10px;line-height:21px;color:#222;display:flex;gap:14px}
.listing .row span{white-space:nowrap}

/* testimonials */
.testi-video{left:99px;top:1612px;width:485px;height:270px;background:linear-gradient(120deg,#8a7564 0%,#5b4b40 50%,#3a302a 100%)}
.quote{position:absolute;left:611px;top:1614px;width:489px;font-size:10.5px;font-style:italic;line-height:22px;color:#555;padding-left:32px}
.quote .mark{position:absolute;font-size:40px;font-style:normal;color:#888;font-weight:700;line-height:1}
.quote cite{position:absolute;right:20px;top:94px;font-style:normal;font-weight:600;color:var(--coral);font-size:12.5px}
.quote-rule{position:absolute;left:611px;top:1735px;width:489px;height:1px;background:#d8c4c4}
.more-title{position:absolute;left:612px;top:1751px;font-size:12.5px;font-weight:600;color:#333}
.more-thumb{position:absolute;top:1783px;height:99px}

/* footer */
.footer{position:absolute;left:0;top:1943px;width:1200px;height:353px;background:var(--dark);color:#ddd}
.footer h4{position:absolute;font-size:20px;font-weight:400;color:var(--white)}
.contact-line{position:absolute;left:213px;font-size:12px;line-height:24px;color:#ccc}
.contact-icon{position:absolute;left:182px;width:14px;height:14px}
.footer-brand{position:absolute;left:182px;top:262px;width:166px;height:56px;background:var(--white);display:flex;align-items:center;justify-content:center;gap:6px}
.footer-brand b{width:14px;height:14px;background:var(--red)}
.footer-brand span{font-size:15px;font-weight:600;color:var(--ink)}
.follow{position:absolute;left:888px;display:flex;align-items:center;gap:20px;font-size:14px;color:#eee}
.follow i{width:50px;height:50px;display:block;background:#5b5557;box-shadow:0 2px 4px rgba(0,0,0,.4)}
.follow i.hot{background:var(--coral)}
.bottom-bar{position:absolute;left:0;top:2296px;width:1200px;height:54px;background:var(--coral);font-size:11px;color:#222;padding:19px 0 0 99px}

.start-card{position:absolute;left:501px;top:1924px;width:270px;height:387px;background:var(--red);border-radius:6px;box-shadow:0 6px 12px rgba(0,0,0,.35)}
.start-card h5{text-align:center;color:var(--white);font-size:21px;font-weight:400;margin-top:12px}
.start-card .sub{text-align:center;color:var(--white);font-size:11px;margin-top:0}
.start-card .inp{position:absolute;left:28px;width:214px;height:33px;background:var(--white);border-radius:3px;font-size:10.5px;color:#888;padding:9px 9px}
.start-card .go{position:absolute;left:28px;top:334px;width:214px;height:31px;background:#2a2424;color:var(--white);font-weight:700;font-size:14px;display:flex;align-items:center;justify-content:center}
</style>
</head>
<body>

<header class="site-header">
  <div class="brand"><span class="brand-mark"></span><span class="brand-name">Velmarhomes.com</span></div>
  <div class="search"><span>Find Apartments ( Enter city, Zip, State or Country )</span>
    <svg width="15" height="15" viewBox="0 0 16 16"><circle cx="6.5" cy="6.5" r="5" fill="none" stroke="#e3222e" stroke-width="2.2"/><path d="M10.3 10.3 15 15" stroke="#e3222e" stroke-width="2.4"/></svg>
  </div>
</header>

<nav class="nav">
  <a class="current" style="left:107px">Home</a>
  <a style="left:191px">About us</a>
  <a style="left:290px">Properties</a>
  <a style="left:398px">Blog</a>
  <a style="left:470px">Contacts</a>
  <span class="dot" style="left:1011px"></span>
  <span class="dot" style="left:1047px"></span>
  <span class="dot" style="left:1082px"></span>
</nav>

<section class="hero">
  <div class="hero-panel">
    <div class="hero-price">$3,50,000<small>only</small></div>
    <div class="hero-street">1180 Harlow Vale</div>
    <div class="hero-facts">DOM: 3 &nbsp;Br: 2 &nbsp;Wsh: 2 &nbsp;Kit: 1<br>List: $300000 &nbsp;Sold: $350000<br>Calculated Over Value: $ 50000</div>
    <div class="hero-btn">More Info</div>
    <div class="hero-dots"><i></i><i></i><i></i><i></i></div>
  </div>
  <div class="hero-photo" role="img" aria-label="Photo of a sold two-storey yellow house with garden and landscaped front yard"></div>
</section>

<section class="welcome">
  <h1>Welcome !</h1>
  <p>Duis aute irure dolor in reprehenderit in voluptate velit esse cillum dolore eu fugiat nulla pariatur. Excepteur sint occaecat cupidatat non proident Lorem ipsum dolor sit amet, consectetuer adipiscing elit, sed diam nonummy nibh euismod tincidunt ut laoreet dolore magna aliquam erat volutpat. Ut wisi enim ad minim ..</p>
  <div class="btn-coral" style="left:122px;top:717px;width:96px;height:30px">Read More</div>
  <div class="divider"></div>
  <div class="explainer" role="img" aria-label="Explainer video still: sketched house with a smiling couple">
    <div class="play sm" style="left:128px;top:64px"><svg viewBox="0 0 10 12"><path d="M0 0 10 6 0 12z" fill="#fff"/></svg></div>
    <div class="bar"><b></b></div>
  </div>
</section>

<section class="band-blush" style="top:788px;height:367px"></section>
<h2 class="section-title" style="left:99px;top:816px">Previously Sold Listings</h2>
<div class="media sold-main" role="img" aria-label="Video still of a modern living room with black shelving and TV wall">
  <div class="play" style="left:220px;top:94px"><svg viewBox="0 0 10 12"><path d="M0 0 10 6 0 12z" fill="#fff"/></svg></div>
  <div class="sold-caption"><span>1452 Corwin Lane.</span><span>Hall: 2</span><span>Br: 4</span><span>Kit: 2</span><span>DOM: 3</span><span>Sold Rate: $ 755,000</span></div>
</div>
<div class="media sold-thumb1" role="img" aria-label="Video still of a bright living room with sofas">
  <div class="play sm" style="left:92px;top:39px"><svg viewBox="0 0 10 12"><path d="M0 0 10 6 0 12z" fill="#fff"/></svg></div>
</div>
<div class="media sold-thumb2" role="img" aria-label="Video still of a dark modern kitchen">
  <div class="play sm" style="left:92px;top:40px"><svg viewBox="0 0 10 12"><path d="M0 0 10 6 0 12z" fill="#fff"/></svg></div>
</div>
<form class="buyer-form">
  <div class="head">Want to buy<br>a home ?</div>
  <div class="field" style="top:100px">Name</div>
  <div class="field" style="top:142px">Email address</div>
  <div class="field select" style="top:184px">Price Range</div>
  <div class="field select" style="top:226px">No. of Br/Hall/Kit</div>
  <div class="field select" style="top:268px">City /Town</div>
  <div class="submit">Submit</div>
</form>

<section class="exclusive">
  <h2 class="section-title" style="left:99px;top:1180px">Exclusive listings</h2>
  <div class="carousel-arrows">
    <span><svg width="10" height="10" viewBox="0 0 10 10"><path d="M7 1 3 5l4 4" fill="none" stroke="#fff" stroke-width="2"/></svg></span>
    <span><svg width="10" height="10" viewBox="0 0 10 10"><path d="M3 1l4 4-4 4" fill="none" stroke="#fff" stroke-width="2"/></svg></span>
  </div>

  <article class="listing" style="left:103px">
    <div class="photo" role="img" aria-label="Bright bathroom with freestanding tub" style="background:linear-gradient(135deg,#d8d8d8,#8c7a60)"><div class="nav-mini"><i></i><i></i></div></div>
    <h3>4120 Ashgrove Crescent</h3>
    <div class="row"><span>DOM: 3</span><span>Br: 3</span><span>Wash: 3</span><span>Kit: 1</span></div>
    <div class="row"><span>List: $500,000</span><span>Sold: $525,000</span></div>
    <div class="row"><span>calculated over asking value in ($): 25000</span></div>
  </article>
  <article class="listing" style="left:354px">
    <div class="photo" role="img" aria-label="Neutral bedroom with framed wall art" style="background:linear-gradient(135deg,#c7b9a1,#6e5a48)"><div class="nav-mini"><i></i><i></i></div></div>
    <h3>3307 Tamberly Road</h3>
    <div class="row"><span>DOM: 3</span><span>Br: 4</span><span>Wash: 4</span><span>Kit: 1</span></div>
    <div class="row"><span>List: $600,000</span><span>Sold: $665,000</span></div>
    <div class="row"><span>calculated over asking value in ($): 65000</span></div>
  </article>
  <article class="listing" style="left:604px">
    <div class="photo" role="img" aria-label="Kitchen with wood cabinets and island" style="background:linear-gradient(135deg,#b48a62,#5a3526)"><div class="nav-mini"><i></i><i></i></div></div>
    <h3>2290 Elsmere Lane</h3>
    <div class="row"><span>DOM: 3</span><span>Br: 4</span><span>Wash: 4</span><span>Kit: 1</span></div>
    <div class="row"><span>List: $600,000</span><span>Sold: $665,000</span></div>
    <div class="row"><span>calculated over asking value in ($): 65000</span></div>
  </article>
  <article class="listing" style="left:855px">
    <div class="photo" role="img" aria-label="Living room with sofas and large windows" style="background:linear-gradient(135deg,#d6c8ad,#8a6e4d)"><div class="nav-mini"><i></i><i></i></div></div>
    <h3>2618 Winfield Lane</h3>
    <div class="row"><span>DOM: 3</span><span>Br: 4</span><span>Wash: 4</span><span>Kit: 1</span></div>
    <div class="row"><span>List: $600,000</span><span>Sold: $665,000</span></div>
    <div class="row"><span>calculated over asking value in ($): 65000</span></div>
  </article>
</section>

<section class="band-blush" style="top:1532px;height:411px"></section>
<h2 class="section-title" style="left:99px;top:1563px">Testimonials</h2>
<svg class="abs" style="left:1084px;top:1571px" width="14" height="14" viewBox="0 0 14 14"><circle cx="7" cy="7" r="7" fill="#bbb"/><path d="M5.5 4l3 3-3 3" fill="none" stroke="#fff" stroke-width="1.6"/></svg>
<div class="media testi-video" role="img" aria-label="Testimonial video still of a couple at a laptop">
  <div class="play" style="left:220px;top:113px"><svg viewBox="0 0 10 12"><path d="M0 0 10 6 0 12z" fill="#fff"/></svg></div>
</div>
<blockquote class="quote">
  <span class="mark" style="left:0;top:-2px">&ldquo;</span>
  Aenean sed quam non sapien faucibus consequat vitae sit amet orci. Praesent quis risus mi. In mollis nulla in pulvinar dictum. Vivamus interdum sagittis felis, ut dapibus ligula feugiat ac. In dictum sapien eu tellus finibus fermentum. Aenean faucibus lacus ut mollis commodo. Donec vestibulum odio sem, ac laoreet massa ullamcorper id massa lacinia.
  <span class="mark" style="left:300px;top:84px">&rdquo;</span>
  <cite>Marcus Dell, Toronto</cite>
</blockquote>
<div class="quote-rule"></div>
<div class="more-title">More Testimonials</div>
<div class="more-thumb" role="img" aria-label="Testimonial video still of a past client" style="left:612px;width:118px;background:linear-gradient(135deg,#8d7a6d,#4a3d36)"><div class="play sm" style="left:43px;top:34px"><svg viewBox="0 0 10 12"><path d="M0 0 10 6 0 12z" fill="#fff"/></svg></div></div>
<div class="more-thumb" role="img" aria-label="Testimonial video still of a past client" style="left:736px;width:118px;background:linear-gradient(135deg,#7b6a5c,#3d332c)"><div class="play sm" style="left:43px;top:34px"><svg viewBox="0 0 10 12"><path d="M0 0 10 6 0 12z" fill="#fff"/></svg></div></div>
<div class="more-thumb" role="img" aria-label="Testimonial video still of a couple" style="left:860px;width:116px;background:linear-gradient(135deg,#9a8878,#514437)"><div class="play sm" style="left:42px;top:34px"><svg viewBox="0 0 10 12"><path d="M0 0 10 6 0 12z" fill="#fff"/></svg></div></div>
<div class="more-thumb" role="img" aria-label="Testimonial video still of a couple" style="left:982px;width:118px;background:linear-gradient(135deg,#8a7e74,#443a33)"><div class="play sm" style="left:43px;top:34px"><svg viewBox="0 0 10 12"><path d="M0 0 10 6 0 12z" fill="#fff"/></svg></div></div>

<footer class="footer">
  <h4 style="left:182px;top:14px">Contact US</h4>
  <svg class="contact-icon" style="top:70px" viewBox="0 0 14 14"><path d="M7 0C4.2 0 2 2.2 2 5c0 3.8 5 9 5 9s5-5.2 5-9c0-2.8-2.2-5-5-5zm0 7a2 2 0 1 1 0-4 2 2 0 0 1 0 4z" fill="#ee5a63"/></svg>
  <div class="contact-line" style="top:63px">Velmar Homes Ltd. 2875<br>Kestrel Crescent Toronto,<br>ON M4B 2K7</div>
  <svg class="contact-icon" style="top:159px" viewBox="0 0 14 14"><path d="M3 1l2.5 3-1.3 1.4c.8 1.8 2.2 3.2 4 4L9.6 8 13 10.4 11.6 13C6 12.6 1.4 8 1 2.4z" fill="#ee5a63"/></svg>
  <div class="contact-line" style="top:153px">Phone:(416) 555-0182</div>
  <svg class="contact-icon" style="top:202px" viewBox="0 0 14 14"><rect x="1" y="5" width="12" height="7" rx="1" fill="#ee5a63"/><rect x="3.5" y="1" width="7" height="5" fill="#ee5a63"/></svg>
  <div class="contact-line" style="top:196px">Fax:(416) 555-0147</div>
  <div class="footer-brand"><b></b><span>Velmarhomes.com</span></div>

  <h4 style="left:888px;top:14px">Follow us</h4>
  <div class="follow" style="top:72px"><i class="hot"></i>Friendwall</div>
  <div class="follow" style="top:145px"><i></i>Circleplus</div>
  <div class="follow" style="top:217px"><i></i>Chirpline</div>
</footer>

<div class="bottom-bar">© 2015 Velmar Homes | Privacy Policy</div>

<form class="start-card">
  <h5>GET STARTED</h5>
  <div class="sub">PLEASE FILL OUT THE BELOW FORM</div>
  <div class="inp" style="top:72px">First Name</div>
  <div class="inp" style="top:111px">Last Name</div>
  <div class="inp" style="top:150px">Email Address</div>
  <div class="inp" style="top:189px">Phone Number</div>
  <div class="inp" style="top:228px;height:88px">Message</div>
  <div class="go">SUBMIT HERE</div>
</form>

</body>
</html>
```